Media Company's Events Website Needs a Design

International Media Company is setting up a new website to market own and partners' events in the Asia Pacific region.

The sitemap and sections are described in the attached document. Supporting images, logos and layout for the mockups are also provided.

We require design mockups for 4 key pages. Please submit homepage mockup for evaluation first. We will give the go-ahead for the other 3 pages once your homepage design is approved, so you do not have to waste unnecessary time.

Any question which I did not cover, please email dale+artmarket@veltronix.biz. Thanks!
Updates

Hi all designers, our client has decided to simplify the website, dropping 2 event categories and focusing on just 1 (i.e. Lumen Crest). 

I am uploading a new homepage layout doc. 

Specifically, changes are:
- New set of tabs on the main menu
- Content area will include: (i) testimonial slider; (ii) video block; (iii) list of upcoming events. feel free to play around with the layout.

Thanks and sorry for the trouble!
Dale

Hi all designers, I have re-uploaded the new brief with respect to the section changes.

Please download and refer to the changes.

Thanks!

Target Market(s)

Corporations, Businessmen, C-level Executives

Industry/Entity Type

Events

Requirements
Must have
• Refer to layout document
Nice to have
• The website may be implemented using WordPress, so a typical 1- and 2-column layout would be deployment-friendly.

```html
<!DOCTYPE html>
<html lang="en">
<head>
<meta charset="utf-8">
<title>Lumen Crest – Events</title>
<link href="https://fonts.googleapis.com/css2?family=Arimo:wght@400;700&family=Tinos:wght@700&display=swap" rel="stylesheet">
<style>
:root{
  --sky:#2d93cf;
  --nav-active:#1c5a86;
  --hero-bg:#ebebeb;
  --ink:#333333;
  --link-blue:#1a6ea8;
  --green:#3f8a12;
  --red:#c8151b;
  --footer:#1e4464;
  --footer-line:#35597a;
  --footer-text:#e3ebf2;
}
*{box-sizing:border-box;margin:0;padding:0}
html,body{width:1090px;height:1200px;overflow:hidden;background:#fff;font-family:"Arimo",Arial,sans-serif;color:var(--ink)}
.page{position:relative;width:1090px;height:1200px}

/* header */
.site-header{position:absolute;left:0;top:0;width:1090px;height:123px;background:radial-gradient(ellipse 300px 90px at 320px 45px,#5fb3e4 0%,var(--sky) 70%)}
.brand{position:absolute;left:155px;top:26px;display:flex;align-items:center;gap:8px}
.brand-name{font-size:36px;color:#4a4a4a;letter-spacing:-1px;font-weight:400}
.brand-dot{width:14px;height:14px;border-radius:50%;background:#f0a020;margin-top:-22px}
.account{position:absolute;left:844px;top:0;height:23px;width:95px;background:#1b4f78;color:#fff;font-size:11px;display:flex;align-items:center;justify-content:center;gap:6px}
.main-nav{position:absolute;left:153px;top:88px;height:35px;display:flex;border:1px solid #1f6fa5;border-bottom:none}
.main-nav a{display:flex;align-items:center;justify-content:center;color:#fff;font-size:12px;text-decoration:none;border-right:1px solid #1f6fa5;background:rgba(255,255,255,.04)}
.main-nav a:last-child{border-right:none}
.main-nav a.active{background:var(--nav-active)}

/* hero testimonial */
.hero{position:absolute;left:0;top:123px;width:1090px;height:308px;background:var(--hero-bg);border-bottom:2px solid #d3d3d3}
.hero-photo{position:absolute;left:211px;top:27px;width:222px;height:257px;border:3px solid #fff;background:linear-gradient(180deg,#9a7e5c 0%,#6b5238 55%,#2a2a30 100%);box-shadow:0 6px 14px rgba(0,0,0,.25)}
.slide-arrow{position:absolute;top:119px;width:36px;height:36px}
.quote-mark{position:absolute;left:464px;top:30px;font-family:"Tinos",serif;font-size:84px;line-height:1;color:#333}
.quote-text{position:absolute;left:488px;top:67px;width:420px;font-size:18px;line-height:22.6px;color:#1872b4;text-indent:36px}
.quote-rule{position:absolute;left:488px;top:198px;width:418px;border-top:1px dotted #8a8a8a}
.quote-author{position:absolute;left:487px;top:212px;font-size:20px;line-height:25px;color:#333}
.quote-author .org{color:var(--red)}

/* events */
.section-title{position:absolute;left:153px;top:471px;font-size:18px;font-weight:400;color:#333}
.event{position:absolute;width:218px;height:100px;border-bottom:1px dotted #666}
.event h3{font-size:14px;font-weight:700;color:var(--link-blue);text-transform:uppercase;letter-spacing:.1px}
.event .city{position:absolute;left:65px;top:25px;font-size:17px;font-weight:700;color:#111}
.event .more{position:absolute;left:67px;top:50px;font-size:15px;color:var(--green)}
.event .attend{position:absolute;left:67px;top:69px;font-size:15px;color:var(--red)}
.cal{position:absolute;left:1px;top:22px;width:52px;height:58px;background:linear-gradient(180deg,#f6f6f6,#dcdcdc);box-shadow:1px 1px 2px rgba(0,0,0,.3)}
.cal .month{height:14px;margin-top:4px;background:#a8161b;color:#fff;font-size:9px;text-align:center;line-height:14px}
.cal .rings{position:absolute;left:4px;top:0;width:44px;height:6px;background:repeating-linear-gradient(90deg,#777 0 1px,transparent 1px 5px)}
.cal .day{font-family:"Tinos",serif;font-weight:700;font-size:25px;text-align:center;color:#444;line-height:36px}

/* sidebar */
.promo{position:absolute;left:722px;width:216px;height:79px;display:flex;align-items:center;overflow:hidden}
.promo-past{top:474px;background:linear-gradient(180deg,#2fb8ee,#1272b4);color:#fff;text-transform:uppercase}
.promo-media{top:577px;background:linear-gradient(180deg,#fafafa,#dedede);border:1px solid #ccc;color:#333;justify-content:center;text-align:center;font-size:19px;line-height:21px;font-variant:small-caps}
.promo-partner{top:680px;background:linear-gradient(180deg,#6dbb2a,#2f8a12);color:#fff;text-transform:uppercase}
.promo-contact{top:781px;background:linear-gradient(180deg,#e4282a,#b20d12);color:#fff}
.promo-art{width:52px;height:48px;margin:0 16px 0 22px;border-radius:4px;flex:none}

/* footer */
.site-footer{position:absolute;left:0;top:1012px;width:1090px;height:188px;background:var(--footer);color:var(--footer-text)}
.f-col{position:absolute;top:24px}
.f-col h4{font-size:12px;font-weight:400;color:#fff;margin-bottom:12px}
.f-col li{list-style:none;font-size:10.5px;line-height:20.5px}
.newsletter p{font-size:10.5px;line-height:12.5px;width:222px;margin-top:-2px}
.signup{margin-top:9px;display:flex;width:218px;height:24px}
.signup .field{flex:1;background:#11304a;font-size:12px;color:#fff;padding-left:7px;line-height:24px}
.signup .btn{width:59px;background:var(--red);color:#fff;font-size:12px;text-align:center;line-height:24px}
.f-rule{position:absolute;left:153px;top:138px;width:785px;border-top:1px solid var(--footer-line)}
.copyright{position:absolute;left:153px;top:153px;font-size:10.5px}
</style>
</head>
<body>
<div class="page">

  <header class="site-header">
    <div class="brand"><span class="brand-name">Lumen Crest</span><span class="brand-dot"></span></div>
    <div class="account"><span>Login</span><span>|</span><span>Register</span></div>
    <nav class="main-nav">
      <a style="width:77px">Home</a>
      <a style="width:183px">About Lumen Crest</a>
      <a style="width:142px">Upcoming Events</a>
      <a class="active" style="width:116px">Past Events</a>
      <a style="width:85px">Videos</a>
      <a style="width:182px">Partnership Opportunities</a>
    </nav>
  </header>

  <section class="hero">
    <svg class="slide-arrow" style="left:131px" viewBox="0 0 36 36"><circle cx="18" cy="18" r="18" fill="#777"/><path d="M22 10 L11 18 L22 26Z" fill="#fff"/></svg>
    <div class="hero-photo" role="img" aria-label="Photo of the speaker presenting at a microphone"></div>
    <div class="quote-mark">&ldquo;</div>
    <p class="quote-text">What’s great about Hangzhou and having offi-cials from the city come to San Francisco to share their ideas, we learn a lot about IP protection, about their real investment in making it a really clean and global city.</p>
    <div class="quote-rule"></div>
    <p class="quote-author">Martin Hale, Chief Commercial Officer,<br><span class="org">Solaris Grid</span></p>
    <svg class="slide-arrow" style="left:925px" viewBox="0 0 36 36"><circle cx="18" cy="18" r="18" fill="#777"/><path d="M14 10 L25 18 L14 26Z" fill="#fff"/></svg>
  </section>

  <h2 class="section-title">Upcoming Events</h2>

  <main>
    <div class="event" style="left:154px;top:510px"><h3>Inside Asia’s Tomorrow</h3><div class="cal"><div class="rings"></div><div class="month">September</div><div class="day">12</div></div><span class="city">Tianjin, China</span><span class="more">Find out more</span><span class="attend">Attend the event</span></div>
    <div class="event" style="left:154px;top:626px"><h3>Energy Forum Asia</h3><div class="cal"><div class="rings"></div><div class="month">October</div><div class="day">3-5</div></div><span class="city">Bangkok, Thailand</span><span class="more">Find out more</span><span class="attend">Attend the event</span></div>
    <div class="event" style="left:154px;top:741px"><h3>Inside Asia’s Tomorrow</h3><div class="cal"><div class="rings"></div><div class="month">September</div><div class="day">12</div></div><span class="city">Tianjin, China</span><span class="more">Find out more</span><span class="attend">Attend the event</span></div>
    <div class="event" style="left:154px;top:857px;border-bottom:none"><h3>Energy Forum Asia</h3><div class="cal"><div class="rings"></div><div class="month">October</div><div class="day">3-5</div></div><span class="city">Bangkok, Thailand</span><span class="more">Find out more</span><span class="attend">Attend the event</span></div>
    <div class="event" style="left:459px;top:510px"><h3>Inside Asia’s Tomorrow</h3><div class="cal"><div class="rings"></div><div class="month">September</div><div class="day">12</div></div><span class="city">Tianjin, China</span><span class="more">Find out more</span><span class="attend">Attend the event</span></div>
    <div class="event" style="left:459px;top:626px"><h3>Energy Forum Asia</h3><div class="cal"><div class="rings"></div><div class="month">October</div><div class="day">3-5</div></div><span class="city">Bangkok, Thailand</span><span class="more">Find out more</span><span class="attend">Attend the event</span></div>
    <div class="event" style="left:459px;top:741px"><h3>Inside Asia’s Tomorrow</h3><div class="cal"><div class="rings"></div><div class="month">September</div><div class="day">12</div></div><span class="city">Tianjin, China</span><span class="more">Find out more</span><span class="attend">Attend the event</span></div>
    <div class="event" style="left:459px;top:857px;border-bottom:none"><h3>Energy Forum Asia</h3><div class="cal"><div class="rings"></div><div class="month">October</div><div class="day">3-5</div></div><span class="city">Bangkok, Thailand</span><span class="more">Find out more</span><span class="attend">Attend the event</span></div>
  </main>

  <aside>
    <div class="promo promo-past"><div class="promo-art" role="img" aria-label="Wall calendar illustration" style="background:linear-gradient(180deg,#e8efe0,#b9c7a8)"></div><div style="font-size:21px;line-height:21px">Past<br><span style="font-size:27px">Events</span></div></div>
    <div class="promo promo-media"><div>View photos and videos<br>FROM THE EVENT</div></div>
    <div class="promo promo-partner"><div class="promo-art" role="img" aria-label="Handshake illustration" style="background:linear-gradient(180deg,#d9c3a8,#8f7a63);margin:0 10px 0 14px;width:46px"></div><div style="font-size:16px;line-height:18px;font-weight:700">Partnership<br>Opportunities</div></div>
    <div class="promo promo-contact"><div style="font-size:17px;line-height:18px;font-weight:700;margin-left:22px;font-variant:small-caps">Contact Orvane<br>LUMEN CREST</div><div class="promo-art" role="img" aria-label="Envelope illustration" style="background:linear-gradient(180deg,#f7b35a,#e07a20);margin:0 12px 0 auto;width:40px"></div></div>
  </aside>

  <footer class="site-footer">
    <div class="f-col" style="left:153px"><h4>Events</h4><ul><li>Strategic Events</li><li>Lumen Crest</li><li>Partner Events</li></ul></div>
    <div class="f-col" style="left:308px"><h4>Join Us</h4><ul><li>Login</li><li>Register</li></ul></div>
    <div class="f-col" style="left:432px"><h4>Connect with us</h4><ul><li>Friendline</li><li>Chirpnet</li><li>Workweb</li></ul></div>
    <div class="f-col" style="left:591px"><h4>Help</h4><ul><li>Contact us</li><li>Privacy Policy</li><li>Sitemap</li></ul></div>
    <div class="f-col newsletter" style="left:722px"><h4>Newsletter Signup</h4><p>Lorem ipsum dolor sit amet, consectetur adipi scing elit. Integer quis libero nisi.</p><div class="signup"><span class="field">your email</span><span class="btn">signup</span></div></div>
    <div class="f-rule"></div>
    <p class="copyright">Copyright © 2012 Lumen Crest. All Right Reserved</p>
  </footer>

</div>
</body>
</html>
```